We want to design total new business card and logo for Kestrel Building Services Ltd

Our company name Kestrel Building Services Ltd. Design new logo and business card , need hi-end luxury style art for architecture and construction industry. The card should simple but stylish. Our business focus on CONNECT tradesman to construction company, help marketing construction company tender oversea projects, managing franchise in construction sector, delivery amazing services to our client, so Logo should show the CONNECTION IDEA, CONNECTING PEOPLE, LUXURY. Visit our website for more information: kestrelhub.co.nz

Low design quality

Target Market(s)

Directors or managers

Industry/Entity Type

Construction Company

Contact Information for Business Card

Name, Title, Mobile, Email, Website

Font styles to use
Serif

Colors

Designer to choose colors to be used in the design.

Requirements
Must have
• Simple and luxury, connection icon
Nice to have
• Special materials, plastic card, look through,...
• Look new ideas.

```html
<!DOCTYPE html>
<html lang="en">
<head>
<meta charset="utf-8">
<title>Kestrel Building Services Ltd — Business Card</title>
<link rel="stylesheet" href="https://fonts.googleapis.com/css2?family=Libre+Baskerville:wght@400;700&display=swap">
<style>
  :root {
    --bg: #e9ecef;
    --blue: #1a8fd0;
    --teal: #2bb5a4;
    --ink: #8a8f94;
    --name: #1a9ac4;
    --white: #ffffff;
    --card-w: 540px;
    --card-h: 310px;
  }
  * { box-sizing: border-box; margin: 0; padding: 0; }
  html, body { width: 1200px; height: 800px; overflow: hidden; }
  body {
    background: var(--bg);
    font-family: "Libre Baskerville", Georgia, serif;
    display: flex;
    align-items: center;
    justify-content: center;
    gap: 40px;
  }
  .card {
    width: var(--card-w);
    height: var(--card-h);
    border-radius: 22px;
    box-shadow: 0 10px 30px rgba(0,0,0,0.15);
    position: relative;
    overflow: hidden;
  }
  .card-front {
    background: linear-gradient(120deg, var(--blue) 0%, #21a3c0 55%, var(--teal) 100%);
    display: flex;
    align-items: center;
    justify-content: center;
  }
  .brand-front {
    display: flex;
    flex-direction: column;
    align-items: center;
    gap: 14px;
    color: var(--white);
    text-align: center;
  }
  .brand-dot {
    width: 22px; height: 22px;
    border-radius: 50%;
    background: var(--white);
  }
  .brand-name {
    font-weight: 700;
    font-size: 22px;
    letter-spacing: 1.5px;
    text-transform: uppercase;
    line-height: 1.45;
  }
  .card-back {
    background: var(--white);
    display: grid;
    grid-template-columns: 230px 1px 1fr;
    align-items: center;
  }
  .brand-back {
    display: flex;
    flex-direction: column;
    align-items: center;
    gap: 12px;
    color: var(--name);
    text-align: center;
    padding: 0 20px;
  }
  .brand-back .brand-dot { background: var(--name); width: 18px; height: 18px; }
  .brand-back .brand-name { font-size: 15px; letter-spacing: 1px; }
  .divider {
    width: 1px;
    height: 150px;
    background: linear-gradient(var(--teal), var(--blue));
  }
  .details { padding-left: 28px; color: var(--ink); }
  .person-name { color: var(--name); font-weight: 700; font-size: 22px; }
  .person-title { font-size: 12px; margin-top: 2px; }
  .address { font-size: 12px; line-height: 1.55; margin-top: 16px; }
  .contacts { list-style: none; margin-top: 14px; font-size: 12px; }
  .contacts li { display: flex; align-items: center; gap: 8px; margin-top: 5px; }
  .contact-icon { width: 16px; height: 16px; flex: none; }
</style>
</head>
<body>
  <section class="card card-front">
    <div class="brand-front">
      <span class="brand-dot"></span>
      <p class="brand-name">Kestrel<br>Building Services Ltd</p>
    </div>
  </section>

  <section class="card card-back">
    <div class="brand-back">
      <span class="brand-dot"></span>
      <p class="brand-name">Kestrel<br>Building Services Ltd</p>
    </div>
    <span class="divider"></span>
    <div class="details">
      <h1 class="person-name">Mara Whitfield</h1>
      <p class="person-title">Manager</p>
      <p class="address">PO Box 48, Harbour Road<br>Level 2, Auckland 1010</p>
      <ul class="contacts">
        <li>
          <svg class="contact-icon" viewBox="0 0 16 16"><circle cx="8" cy="8" r="8" fill="#1a9ac4"/><rect x="5.5" y="3.5" width="5" height="9" rx="1" fill="none" stroke="#fff" stroke-width="1.2"/></svg>
          021 555 0148
        </li>
        <li>
          <svg class="contact-icon" viewBox="0 0 16 16"><circle cx="8" cy="8" r="8" fill="#1a9ac4"/><rect x="4" y="5" width="8" height="6" fill="none" stroke="#fff" stroke-width="1.2"/><path d="M4 5l4 3.5L12 5" fill="none" stroke="#fff" stroke-width="1.2"/></svg>
          hello@kestrelhub.co.nz
        </li>
        <li>
          <svg class="contact-icon" viewBox="0 0 16 16"><circle cx="8" cy="8" r="8" fill="#1a9ac4"/><circle cx="8" cy="8" r="4" fill="none" stroke="#fff" stroke-width="1.2"/><path d="M4 8h8M8 4v8" stroke="#fff" stroke-width="1"/></svg>
          www.kestrelhub.co.nz
        </li>
      </ul>
    </div>
  </section>
</body>
</html>
```